International Used Food Processing Equipment company needs an awesome website!

We have been in business now for more than 15 years, and we are now launching a new website where international and USA based customers can view photos, descriptions, and ask questions of industrial food processing equipment.

We want the site to be vibrant and but yet communicate a professional tone to our customers. Most of our customers are older males, and the site must be easy to navigate, with easy on the eye color scheme. We want to features a lot of photos and a excellent equipment descriptions, with links where visitors can click on an item to send us a request for more information. We require easy to read font, clear navigation buttons and clear contact information to be found on each page.

Some of our competitors sites:
www.KVPTrade.com
www.lantorvalleyworks.com
www.pelvoxgroup.com

Our business name and logo is attached, but this is a rending of an image that was made about 10 years ago. Please let us know if you have any questions.

Target Market(s)

Food processing companies (canneries, fresh cut sector, large catering companies) in the USA and South America.

Logo Text

Excellent Machines at Excellent Prices

Coding

Coded - Design and coding required

Number of Pages Required

5+ page

Colors

Designer to choose colors to be used in the design.

Requirements
Must have
• Easy to navigate photo galleries, easy category search and easy machine search by keywords.
• Event Calendar
• Sign-up page for email newsletter
Nice to have
• Blog feature or latest news
• Past projects page
Should not have
• Hard to read font

```html
<!DOCTYPE html>
<html lang="en">
<head>
<meta charset="utf-8">
<title>Machinery Steward – Used Food Processing Equipment</title>
<link rel="stylesheet" href="https://fonts.googleapis.com/css2?family=Poppins:wght@300;400;500;600;700&family=Oswald:wght@400;500&display=swap">
<style>
:root{
  --ink:#1d1d1d;
  --text:#555;
  --muted:#888;
  --blue:#1b8fd0;
  --navy:#17375e;
  --teal:#1e8fb0;
  --teal-dark:#0f6f8e;
  --orange:#f7a823;
  --orange-light:#fbb733;
  --light:#f2f2f2;
  --line:#ddd;
  --white:#fff;
}
*{box-sizing:border-box;margin:0;padding:0}
html,body{width:1200px;height:4675px;overflow:hidden}
body{font-family:"Poppins",sans-serif;color:var(--ink);background:var(--white);position:relative}
section,header,footer{position:absolute;left:0;width:1200px}
.abs{position:absolute}
.fill{display:block}

/* header */
.site-header{top:0;height:131px;background:var(--white)}
.brand{left:140px;top:14px;display:flex;align-items:center;gap:12px}
.brand-mark{width:26px;height:26px;border-radius:50%;background:var(--ink)}
.brand-name{font-size:22px;font-weight:600;color:var(--ink)}
.brand-tag{left:178px;top:50px;font-size:11px;color:var(--muted)}
.top-search{left:660px;top:25px;width:222px;height:38px;border:2px solid #333;border-radius:20px;display:flex;align-items:center;gap:10px;padding-left:18px;font-size:14px;color:#333}
.sign-in{left:900px;top:25px;width:154px;height:38px;border:2px solid var(--blue);border-radius:20px;display:flex;align-items:center;justify-content:center;gap:8px;font-size:14px;font-weight:600;color:var(--blue)}
.main-nav{right:146px;top:88px;display:flex;gap:22px;font-size:14px;font-weight:600;color:var(--navy)}

/* hero */
.hero{top:131px;height:555px}
.hero-photo{width:100%;height:100%;background:linear-gradient(120deg,#6f6a62 0%,#a9a39a 35%,#d8d3cb 60%,#8b8780 100%)}
.hero-title{left:0;width:100%;top:190px;text-align:center;font-size:56px;font-weight:600;color:var(--white);letter-spacing:-.5px}
.hero-arrow{top:280px;width:40px;height:40px;border-radius:50%;background:rgba(0,0,0,.45)}
.hero-search{left:243px;top:305px;width:717px;height:80px;background:rgba(20,20,20,.65);display:flex;align-items:center;gap:14px;padding:0 18px}
.field{height:38px;background:var(--white);display:flex;align-items:center;justify-content:space-between;padding:0 12px;font-size:13px;color:var(--muted)}
.field.category{width:250px}
.field.keyword{width:270px}
.btn-search{width:128px;height:38px;background:var(--blue);color:var(--white);font-size:15px;font-weight:600;display:flex;align-items:center;justify-content:center}

/* welcome */
.welcome{top:686px;height:389px;background:var(--light)}
.welcome-figure{left:218px;top:45px;width:205px;height:285px;background:linear-gradient(180deg,#cfcfcf,#8a8a8a);border-radius:6px}
.welcome-copy{left:449px;top:52px;width:560px}
.welcome-kicker{font-size:28px;color:var(--navy);font-weight:500}
.welcome-title{font-size:50px;font-weight:500;color:var(--ink);line-height:1.15}
.welcome-rule{width:95px;height:4px;background:var(--navy);margin:16px 0 18px}
.welcome-copy p{font-size:15px;line-height:1.75;color:var(--text)}

/* events */
.events{top:1075px;height:711px}
.section-title{left:0;width:100%;text-align:center;font-size:44px;font-weight:600;color:var(--ink)}
.events .section-title{top:66px}
.month-bar{left:143px;top:172px;width:911px;height:87px;background:#f5f5f5;border:1px solid var(--line);display:flex;align-items:center;padding:0 28px}
.month-current{font-size:32px;font-weight:500;display:flex;align-items:center;gap:18px}
.stepper{width:36px;height:36px;border:1px solid #ccc;background:var(--white);font-size:14px;display:flex;align-items:center;justify-content:center}
.month-filters{margin-left:auto;display:flex;gap:12px}
.select{height:38px;background:var(--white);border:1px solid #ccc;font-size:13px;display:flex;align-items:center;justify-content:space-between;padding:0 10px;gap:14px}
.select.month{width:120px}.select.year{width:118px}
.btn-show{width:92px;height:38px;background:var(--blue);color:var(--white);font-size:15px;display:flex;align-items:center;justify-content:center}
.carousel-arrow{top:410px;color:#bbb;font-size:40px;font-weight:300}
.event-card{top:290px;width:297px;height:300px;overflow:hidden}
.event-photo{width:100%;height:100%}
.event-overlay{left:0;bottom:0;width:100%;padding:16px 16px 22px;background:linear-gradient(0deg,rgba(0,0,0,.75),rgba(0,0,0,0))}
.event-date{display:inline-block;background:var(--orange);color:var(--white);font-size:12px;padding:3px 9px;margin-bottom:8px}
.event-name{font-family:"Oswald",sans-serif;font-size:16px;line-height:1.3;color:var(--white);text-transform:uppercase}

/* newsletter */
.newsletter{top:1786px;height:468px;background:linear-gradient(90deg,var(--orange) 0%,var(--orange-light) 100%)}
.newsletter-person{left:610px;top:0;width:590px;height:468px;background:linear-gradient(90deg,rgba(255,255,255,0) 0%,rgba(240,225,205,.55) 50%,rgba(255,255,255,.1) 100%)}
.newsletter-copy{left:143px;top:90px;width:470px}
.newsletter-copy h2{font-size:38px;font-weight:700;color:var(--ink);letter-spacing:.5px}
.newsletter-copy p{font-size:17px;line-height:1.65;color:var(--ink);margin-top:14px}
.email-input{left:143px;top:271px;width:468px;height:44px;background:var(--white);border:1px solid #ccc;font-size:13px;color:#555;display:flex;align-items:center;padding-left:18px}
.btn-subscribe{left:143px;top:334px;width:468px;height:44px;background:#1a1a1a;color:var(--white);font-size:18px;font-weight:600;display:flex;align-items:center;justify-content:center}

/* galleries */
.galleries{top:2254px;height:748px}
.galleries .section-title{top:74px}
.gallery-feature{left:143px;top:190px;width:415px;height:411px;border:1px solid var(--line);background:var(--white)}
.gallery-feature .photo{width:100%;height:228px}
.gallery-feature h3{font-size:20px;font-weight:400;text-align:center;line-height:1.45;margin:22px 40px 10px;color:#333}
.gallery-feature p{font-size:13px;line-height:1.7;text-align:center;color:var(--text);margin:0 28px}
.gallery-tile{width:236px;height:200px}

/* news */
.news{top:3002px;height:583px;background:linear-gradient(180deg,var(--teal) 0%,#2a9dbd 100%)}
.news-title{left:0;width:100%;top:86px;text-align:center;font-size:40px;font-weight:600;color:var(--white)}
.news-wave{left:0;bottom:0;width:1200px;height:300px}
.news-card{top:199px;width:287px;height:331px;background:var(--white);border:2px solid var(--blue);border-radius:4px;padding:26px 20px 0 22px}
.news-card h3{font-size:15px;font-weight:500;line-height:1.6;text-transform:uppercase;color:var(--ink)}
.news-date{display:flex;align-items:center;gap:8px;font-size:13px;color:var(--navy);margin:14px 0 12px}
.news-card p{font-size:13px;line-height:1.75;color:#333}
.btn-more{position:absolute;left:50%;transform:translateX(-50%);bottom:-2px;width:124px;height:34px;border:2px solid var(--blue);background:var(--white);font-size:12px;color:var(--navy);display:flex;align-items:center;justify-content:center}

/* reviews */
.reviews{top:3585px;height:551px}
.reviews .section-title{top:75px;font-size:40px}
.reviews-text{left:210px;top:143px;width:780px;text-align:center;font-size:14px;line-height:1.9;color:var(--text)}
.avatar{border-radius:50%;border:3px solid var(--white);box-shadow:0 2px 8px rgba(0,0,0,.25);background:linear-gradient(180deg,#b9b6b2,#6e6a66)}
.reviewer{left:0;width:100%;top:378px;text-align:center;font-size:17px;color:#333}
.quote{top:368px;font-size:52px;color:#bbb;font-family:Georgia,serif;line-height:1}
.dots{left:0;width:100%;top:432px;display:flex;justify-content:center;gap:6px}
.dot{width:14px;height:14px;border-radius:50%;border:2px solid #d33}

/* footer */
.site-footer{top:4136px;height:368px;background:var(--light)}
.footer-figure{left:140px;top:60px;width:130px;height:220px;background:linear-gradient(180deg,#cfcfcf,#8a8a8a);border-radius:6px}
.footer-col h4{font-size:22px;font-weight:600;color:var(--ink);margin-bottom:18px}
.footer-signup{left:330px;top:68px;width:270px}
.footer-signup p{font-size:12px;line-height:1.6;color:var(--text)}
.footer-email{width:270px;height:36px;border:1px solid #ccc;border-radius:20px;background:var(--white);font-size:11px;color:#777;display:flex;align-items:center;padding-left:16px;margin-top:18px}
.footer-sub{width:138px;height:38px;border-radius:20px;background:var(--blue);color:var(--white);font-size:14px;font-weight:600;display:flex;align-items:center;justify-content:center;margin-top:22px}
.footer-contact{left:660px;top:68px;width:240px}
.contact-row{display:flex;gap:14px;font-size:13px;line-height:1.5;color:#333;margin-bottom:16px}
.contact-row svg{flex:none;margin-top:3px}
.footer-links{left:930px;top:68px}
.footer-links li{list-style:none;font-size:13px;color:#333;margin-bottom:14px}
.bottom-bar{top:4504px;height:171px;background:var(--white)}
.copyright{left:0;width:100%;top:52px;text-align:center;font-size:13px;color:#333}
.socials{left:0;width:100%;top:104px;display:flex;justify-content:center;gap:8px}
.social{width:28px;height:28px;border-radius:50%;border:1.5px solid #333}
</style>
</head>
<body>

<header class="site-header">
  <div class="abs brand"><span class="brand-mark"></span><span class="brand-name">Machinery Steward</span></div>
  <div class="abs brand-tag">Excellent Machines at Excellent Prices</div>
  <div class="abs top-search">
    <svg width="16" height="16" viewBox="0 0 16 16"><circle cx="6.5" cy="6.5" r="5" fill="none" stroke="#333" stroke-width="2"/><path d="M10.5 10.5L15 15" stroke="#333" stroke-width="2"/></svg>SEARCH
  </div>
  <div class="abs sign-in">
    <svg width="12" height="14" viewBox="0 0 12 14"><rect x="1" y="6" width="10" height="8" rx="1" fill="#1b8fd0"/><path d="M3 6V4a3 3 0 016 0v2" fill="none" stroke="#1b8fd0" stroke-width="1.8"/></svg>SIGN IN
  </div>
  <nav class="abs main-nav"><span>HOME</span><span>PHOTO GALLERIES</span><span>ABOUT</span><span>EVENTS</span><span>PAST PROJECTS</span><span>CONTACT US</span></nav>
</header>

<section class="hero">
  <div class="hero-photo fill" role="img" aria-label="Food production line with worker inspecting baked goods on conveyor"></div>
  <h1 class="abs hero-title">The Machinery Steward</h1>
  <div class="abs hero-arrow" style="left:76px"><svg width="40" height="40"><path d="M23 13l-7 7 7 7" fill="none" stroke="#fff" stroke-width="2.5"/></svg></div>
  <div class="abs hero-arrow" style="left:1084px"><svg width="40" height="40"><path d="M17 13l7 7-7 7" fill="none" stroke="#fff" stroke-width="2.5"/></svg></div>
  <div class="abs hero-search">
    <div class="field category">Category <span>▾</span></div>
    <div class="field keyword">Search by keywords
      <svg width="13" height="13" viewBox="0 0 16 16"><circle cx="6.5" cy="6.5" r="5" fill="none" stroke="#333" stroke-width="2"/><path d="M10.5 10.5L15 15" stroke="#333" stroke-width="2"/></svg></div>
    <div class="btn-search">SEARCH</div>
  </div>
</section>

<section class="welcome">
  <div class="abs welcome-figure" role="img" aria-label="Illustrated butler gesturing to the welcome text"></div>
  <div class="abs welcome-copy">
    <div class="welcome-kicker">Welcome to</div>
    <div class="welcome-title">Machinery Steward</div>
    <div class="welcome-rule"></div>
    <p>Sed ut perspiciatis unde omnis iste natus error sit voluptatem accusantium doloremque laudantium, totam rem aperiam, eaque ipsa quae ab illo inicre veritatis et quasi architecto beatae vitae dicta sunt explicabo. Nemo enim ipsam voluptatem quia voluptas sit aspernatur aut odit aut fugit, sed quia consequuntur</p>
  </div>
</section>

<section class="events">
  <h2 class="abs section-title">Event Calendar</h2>
  <div class="abs month-bar">
    <div class="month-current">February <span class="stepper">⇕</span></div>
    <div class="month-filters">
      <div class="select month">February <span>▾</span></div>
      <div class="select year">2019 <span>▾</span></div>
      <div class="btn-show">Show</div>
    </div>
  </div>
  <div class="abs carousel-arrow" style="left:82px">‹</div>
  <div class="abs carousel-arrow" style="left:1098px">›</div>

  <article class="abs event-card" style="left:143px">
    <div class="event-photo" role="img" aria-label="Biscuits moving along a factory conveyor" style="background:linear-gradient(160deg,#5a4630,#b98a4f 55%,#3d3224)"></div>
    <div class="abs event-overlay"><span class="event-date">▦ February 5, 2019</span><div class="event-name">Sed ut perspiciatis unde omnis iste natus error sit voluptatem accusantium</div></div>
  </article>
  <article class="abs event-card" style="left:452px">
    <div class="event-photo" role="img" aria-label="Strawberries on a processing line" style="background:linear-gradient(160deg,#2b2224,#a3303a 55%,#3a2c2c)"></div>
    <div class="abs event-overlay"><span class="event-date">▦ February 5, 2019</span><div class="event-name">Sed ut perspiciatis unde omnis iste natus error sit voluptatem accusantium</div></div>
  </article>
  <article class="abs event-card" style="left:760px">
    <div class="event-photo" role="img" aria-label="Stainless steel packaging conveyors" style="background:linear-gradient(160deg,#3a2e26,#9a7a5e 55%,#4a3b30)"></div>
    <div class="abs event-overlay"><span class="event-date">▦ February 5, 2019</span><div class="event-name">Sed ut perspiciatis unde omnis iste natus error sit voluptatem accusantium</div></div>
  </article>
</section>

<section class="newsletter">
  <div class="abs newsletter-person" role="img" aria-label="Excited woman holding a laptop"></div>
  <div class="abs newsletter-copy">
    <h2>JOIN OUR NEWSLETTER</h2>
    <p>Subscribe to our newsletter below to be the first to hear of our next exciting event.Sed ut perspiciatis unde omnis iste natus error sit voluptatem</p>
  </div>
  <div class="abs email-input">Enter your E – mail</div>
  <div class="abs btn-subscribe">SUBSCRIBE</div>
</section>

<section class="galleries">
  <h2 class="abs section-title">PHOTO GALLERIES</h2>
  <article class="abs gallery-feature">
    <div class="photo" role="img" aria-label="Rows of ring biscuits on a production belt" style="background:linear-gradient(150deg,#8c5a25,#d49a55 50%,#a36d33)"></div>
    <h3>Sed ut perspiciatis unde omnis sit voluptatem accusantium</h3>
    <p>Sed ut perspiciatis unde omnis iste natus error sit voluptatem accusantium doloremque laudantium, totam rem aperiam, eaque ipsa quae ab illo inventore veritatis</p>
  </article>
  <div class="abs gallery-tile" style="left:570px;top:190px;background:linear-gradient(150deg,#6e4c43,#c3a69a 50%,#8a6a5e)" role="img" aria-label="Meat processing line"></div>
  <div class="abs gallery-tile" style="left:818px;top:190px;background:linear-gradient(150deg,#2f4a2a,#6f8c4e 50%,#3d4f35)" role="img" aria-label="Jars on a bottling conveyor"></div>
  <div class="abs gallery-tile" style="left:570px;top:401px;background:linear-gradient(150deg,#6b4a2a,#c98f4c 50%,#7b5a3a)" role="img" aria-label="Baked bars on a cooling line"></div>
  <div class="abs gallery-tile" style="left:818px;top:401px;background:linear-gradient(150deg,#44525c,#9aa5ad 50%,#5a6570)" role="img" aria-label="Factory floor with workers at processing machines"></div>
</section>

<section class="news">
  <h2 class="abs news-title">LATEST NEWS</h2>
  <svg class="abs news-wave" viewBox="0 0 1200 300" preserveAspectRatio="none"><path d="M0 130 Q600 -60 1200 130 L1200 300 L0 300Z" fill="#fff"/></svg>
  <article class="abs news-card" style="left:143px">
    <h3>Sed ut perspiciatis unde omnis iste natus</h3>
    <div class="news-date"><svg width="13" height="13" viewBox="0 0 13 13"><rect x="1" y="2" width="11" height="10" fill="none" stroke="#17375e" stroke-width="1.4"/><path d="M1 5h11" stroke="#17375e" stroke-width="1.4"/></svg>Feb 3, 2019</div>
    <p>Sed ut perspiciatis unde omnis iste natus error sit voluptatem accusantium doloremque laudantium, totam rem aperiam, eaque ipsa quae ab illo itore veritatis et quasi architecto</p>
    <div class="btn-more">READ MORE</div>
  </article>
  <article class="abs news-card" style="left:455px">
    <h3>Sed ut perspiciatis unde omnis iste natus</h3>
    <div class="news-date"><svg width="13" height="13" viewBox="0 0 13 13"><rect x="1" y="2" width="11" height="10" fill="none" stroke="#17375e" stroke-width="1.4"/><path d="M1 5h11" stroke="#17375e" stroke-width="1.4"/></svg>Feb 3, 2019</div>
    <p>Sed ut perspiciatis unde omnis iste natus error sit voluptatem accusantium doloremque laudantium, totam rem aperiam, eaque ipsa quae ab illo itore veritatis et quasi architecto</p>
    <div class="btn-more">READ MORE</div>
  </article>
  <article class="abs news-card" style="left:767px">
    <h3>Sed ut perspiciatis unde omnis iste natus</h3>
    <div class="news-date"><svg width="13" height="13" viewBox="0 0 13 13"><rect x="1" y="2" width="11" height="10" fill="none" stroke="#17375e" stroke-width="1.4"/><path d="M1 5h11" stroke="#17375e" stroke-width="1.4"/></svg>Feb 3, 2019</div>
    <p>Sed ut perspiciatis unde omnis iste natus error sit voluptatem accusantium doloremque laudantium, totam rem aperiam, eaque ipsa quae ab illo itore veritatis et quasi architecto</p>
    <div class="btn-more">READ MORE</div>
  </article>
</section>

<section class="reviews">
  <h2 class="abs section-title">Customers Reviews</h2>
  <p class="abs reviews-text">Sed ut perspiciatis unde omnis iste natus error sit voluptatem accusantium doloremque laudantium, totam rem aperiam, eaque ipsa quae ab illo inventore veritatis et quasi architecto beatae vitae dicta sunt explicabo. Nemo enim ipsam voluptatem quia voluptas sit aspernatur aut odit aut fugit Sed ut perspiciatis unde omnis</p>
  <div class="abs avatar" style="left:460px;top:270px;width:66px;height:66px" role="img" aria-label="Customer portrait"></div>
  <div class="abs avatar" style="left:548px;top:252px;width:104px;height:104px" role="img" aria-label="Featured customer portrait"></div>
  <div class="abs avatar" style="left:674px;top:270px;width:66px;height:66px" role="img" aria-label="Customer portrait"></div>
  <div class="abs quote" style="left:494px">“</div>
  <div class="abs quote" style="left:676px">”</div>
  <div class="abs reviewer">Blandit Lectus</div>
  <div class="abs dots"><span class="dot"></span><span class="dot"></span><span class="dot"></span></div>
</section>

<footer class="site-footer">
  <div class="abs footer-figure" role="img" aria-label="Illustrated butler figure"></div>
  <div class="abs footer-col footer-signup">
    <h4>sign up for newsletter</h4>
    <p>excepteur sint occaecat cupidatat non proident, sunt in culpa qui officia deserunt</p>
    <div class="footer-email">Enter email</div>
    <div class="footer-sub">SUBSCRIBE</div>
  </div>
  <div class="abs footer-col footer-contact">
    <h4>contact us</h4>
    <div class="contact-row"><svg width="14" height="18" viewBox="0 0 14 18"><path d="M7 1a6 6 0 00-6 6c0 4.5 6 10 6 10s6-5.5 6-10a6 6 0 00-6-6z" fill="#1b8fd0"/><circle cx="7" cy="7" r="2.2" fill="#fff"/></svg><span>Machinery Steward<br>Road Kelmont Park, WA</span></div>
    <div class="contact-row"><svg width="16" height="16" viewBox="0 0 16 16"><path d="M3 1l3 3-2 2c1 2 3 4 5 5l2-2 3 3-2 3C7 15 1 9 1 3z" fill="#1b8fd0"/></svg><span>Phone<br>08 5550 1290</span></div>
    <div class="contact-row"><svg width="16" height="13" viewBox="0 0 16 13"><rect x="0.5" y="0.5" width="15" height="12" fill="#1b8fd0"/><path d="M1 1l7 6 7-6" fill="none" stroke="#fff" stroke-width="1.3"/></svg><span>Email:<br>info@machinerysteward.com</span></div>
  </div>
  <div class="abs footer-col footer-links">
    <h4>quick links</h4>
    <ul><li>Home</li><li>Photo Galleries</li><li>About</li><li>Events</li><li>Past Projects</li><li>Contact</li></ul>
  </div>
</footer>

<section class="bottom-bar">
  <p class="abs copyright">Machinery Steward © 2019 All Rights Reserved | Privacy Policy | Terms and Conditions</p>
  <div class="abs socials"><span class="social"></span><span class="social"></span><span class="social"></span><span class="social"></span></div>
</section>

</body>
</html>
```